Werbe Banner für ein Malerbetrieb
Zielgruppe
Wir Bieten Dienstleistungen rund ums Haus Hauptsächlich für Privat Kunden u. Gewerbekunden.
Durschnitts Alter der Kundschaft 50-60 Jahren
Aufgabenstellung
soll zur Neu Kunden Gewinnung dienen, Von der Konkurrenz Unterscheiden, Auffallen, Elegant, Gut Lesbar auch von weiter Entfernung, nicht überladen die werbe banner werden an Hauptstraßen angebracht.

```html
<!DOCTYPE html>
<html lang="de">
<head>
<meta charset="utf-8">
<title>Pinselhaus – Zeit für einen neuen Anstrich</title>
<link rel="stylesheet" href="https://fonts.googleapis.com/css2?family=Anton&family=Crimson+Pro:ital,wght@0,500;1,600&display=swap">
<style>
  :root {
    --bg: #222222;
    --white: #ffffff;
    --brand-blue: #0088d1;
    --paint-red: #c0101a;
    --paint-green: #a3c03a;
    --paint-blue: #0088d1;
    --paint-yellow: #f3d212;
    --paint-orange: #dd931c;
    --paint-teal: #7abcc2;
  }
  html, body {
    margin: 0;
    padding: 0;
    width: 1200px;
    height: 1200px;
    overflow: hidden;
    background: var(--bg);
  }
  .banner {
    display: block;
    width: 1200px;
    height: 1200px;
  }
  .headline {
    font-family: "Anton", "Arial Narrow", sans-serif;
    fill: var(--white);
  }
  .brand-name {
    font-family: "Anton", "Arial Narrow", sans-serif;
    fill: var(--brand-blue);
  }
  .tagline {
    font-family: "Crimson Pro", Georgia, serif;
    font-style: italic;
    font-weight: 600;
    fill: var(--white);
  }
  .contact-band { fill: var(--brand-blue); }
  .contact-line {
    font-family: "Crimson Pro", Georgia, serif;
    font-weight: 500;
    fill: var(--white);
  }
</style>
</head>
<body>
<svg class="banner" viewBox="0 0 1200 1200" xmlns="http://www.w3.org/2000/svg">
  <defs>
    <linearGradient id="splash-top-tones" x1="0" y1="0" x2="1" y2="0">
      <stop offset="0" stop-color="var(--paint-red)"/>
      <stop offset="0.3" stop-color="var(--paint-red)"/>
      <stop offset="0.45" stop-color="var(--paint-green)"/>
      <stop offset="0.65" stop-color="var(--paint-blue)"/>
      <stop offset="0.85" stop-color="var(--paint-yellow)"/>
      <stop offset="1" stop-color="var(--paint-yellow)"/>
    </linearGradient>
    <linearGradient id="splash-bottom-tones" x1="0" y1="0" x2="1" y2="0">
      <stop offset="0" stop-color="var(--paint-orange)"/>
      <stop offset="0.3" stop-color="var(--paint-red)"/>
      <stop offset="0.5" stop-color="var(--paint-yellow)"/>
      <stop offset="0.7" stop-color="var(--paint-teal)"/>
      <stop offset="1" stop-color="var(--paint-teal)"/>
    </linearGradient>
  </defs>

  <rect class="background" width="1200" height="1200" fill="var(--bg)"/>

  <rect class="paint-splash paint-splash--top" x="109" y="19" width="966" height="316" rx="40"
        fill="url(#splash-top-tones)" role="img"
        aria-label="Farbkleckse in Rot, Grün, Blau und Gelb über der Überschrift"/>

  <text class="headline" x="152" y="503" font-size="120" textLength="888" lengthAdjust="spacingAndGlyphs">ZEIT FÜR EINEN</text>
  <text class="headline" x="79" y="657" font-size="120" textLength="1042" lengthAdjust="spacingAndGlyphs">NEUEN ANSTRICH</text>

  <rect class="paint-splash paint-splash--bottom" x="90" y="690" width="1022" height="176" rx="30"
        fill="url(#splash-bottom-tones)" role="img"
        aria-label="Farbkleckse in Orange, Rot, Gelb und Türkis mit herablaufenden Tropfen"/>

  <text class="brand-name" x="197" y="999" font-size="89" textLength="803" lengthAdjust="spacingAndGlyphs">PINSELHAUS</text>

  <text class="tagline" x="600" y="1068" font-size="58" text-anchor="middle">Farbe, die Freude macht.</text>

  <rect class="contact-band" x="0" y="1112" width="1200" height="88"/>
  <text class="contact-line" x="42" y="1170" font-size="48" textLength="1115" lengthAdjust="spacingAndGlyphs">fon: +49 (0)7141 5093826 • www.pinselhaus-lb.de</text>
</svg>
</body>
</html>
```